Can Design for Fun, Growing Health Food Brand

We are launching a brand new product, electrolyte seltzer drinks. We want the design to be clean/simple and slightly modern while staying true to our brand identity. Must say "Mineral Hydration" as the product descriptor, sub headline is "Carbonated electrolyte beverage with sea moss and real fruit juice". First flavors will be Watermelon Mint and Mango.

Target Market(s)

Women ages 30-50 who are interested in health wellness/trends

Industry/Entity Type

Health & Wellness

Font styles to use
Sans Serif

Requirements
Must have
• Tall, skinny can, current Brightfen Kelp Logo, use aluminum on can as element in design.
Nice to have
• Be fun, clean and modern. Would like to see the label less busy than our gels.
Should not have
• Avoid putting flavor on bottom 1/5 of can. No gradient color changes. Do not want really detailed or realistic fruit image, prefer drawings or similar.

```html
<!DOCTYPE html>
<html lang="en">
<head>
<meta charset="utf-8">
<title>Brightfen Kelp – Mineral Hydration Mango Label</title>
<link rel="stylesheet" href="https://fonts.googleapis.com/css2?family=Montserrat:wght@400;500&family=Roboto+Condensed:wght@400;500&display=swap">
<style>
  :root {
    --backdrop: #b3b3b3;
    --label: #ffffff;
    --brand-grey: #808184;
    --accent: #d8862a;
    --ink: #111111;
    --mango-light: #fcc124;
    --mango-deep: #e2a12b;
  }
  * { margin: 0; padding: 0; box-sizing: border-box; }
  html, body {
    width: 1200px;
    height: 2302px;
    overflow: hidden;
    background: var(--backdrop);
  }
  .label {
    position: absolute;
    left: 66px;
    top: 94px;
    width: 1068px;
    height: 2114px;
    background: var(--label);
    text-align: center;
  }
  .label > * { position: absolute; left: 0; width: 100%; }
  .brand-mark {
    left: 474px;
    top: 234px;
    width: 120px;
    height: 120px;
    border: 10px solid var(--brand-grey);
    border-radius: 50%;
  }
  .brand-name {
    top: 500px;
    font-family: "Roboto Condensed", sans-serif;
    font-weight: 400;
    font-size: 124px;
    line-height: 1;
    letter-spacing: -2px;
    color: var(--brand-grey);
  }
  .descriptor {
    top: 660px;
    font-family: "Montserrat", sans-serif;
    font-weight: 500;
    font-size: 54px;
    letter-spacing: 5px;
    color: var(--accent);
  }
  .subline {
    top: 766px;
    font-family: "Montserrat", sans-serif;
    font-weight: 400;
    font-size: 39px;
    line-height: 58px;
    color: var(--ink);
  }
  .flavor-art {
    left: 328px;
    top: 924px;
    width: 412px;
    height: 482px;
    border-radius: 48% 48% 44% 44%;
    background: radial-gradient(ellipse at 45% 45%, var(--mango-light), var(--mango-deep));
  }
  .flavor-name {
    top: 1486px;
    font-family: "Montserrat", sans-serif;
    font-weight: 500;
    font-size: 64px;
    letter-spacing: 8px;
    color: var(--accent);
  }
  .claims {
    top: 1688px;
    height: 184px;
  }
  .claim {
    position: absolute;
    top: 0;
    width: 184px;
    height: 184px;
    border: 4px solid var(--accent);
    border-radius: 50%;
    display: flex;
    flex-direction: column;
    align-items: center;
    justify-content: center;
    font-family: "Roboto Condensed", sans-serif;
    font-size: 36px;
    line-height: 48px;
    letter-spacing: 3px;
    color: var(--accent);
  }
  .claim--sugar { left: 172px; }
  .claim--plant { left: 416px; }
  .claim--electrolytes { left: 676px; }
  .claim--electrolytes span {
    background: var(--label);
    padding: 0 4px;
    white-space: nowrap;
  }
  .volume {
    top: 1958px;
    font-family: "Roboto Condensed", sans-serif;
    font-weight: 500;
    font-size: 54px;
    letter-spacing: 3px;
    color: var(--ink);
  }
</style>
</head>
<body>
  <main class="label">
    <div class="brand-mark" aria-hidden="true"></div>
    <h1 class="brand-name">Brightfen Kelp</h1>
    <p class="descriptor">MINERAL HYDRATION</p>
    <p class="subline">Carbonated electrolyte beverage<br>with sea moss and real fruit juice</p>
    <div class="flavor-art" role="img" aria-label="Drawing of a whole mango with leaves and a cubed mango half"></div>
    <p class="flavor-name">MANGO</p>
    <div class="claims">
      <div class="claim claim--sugar"><span>NO</span><span>SUGAR</span></div>
      <div class="claim claim--plant"><span>PLANT</span><span>BASED</span></div>
      <div class="claim claim--electrolytes"><span>900MG</span><span>ELECTROLYTES</span></div>
    </div>
    <p class="volume">250ml</p>
  </main>
</body>
</html>
```